Bidwave Set Up Ads for VELTA Property Management Company

We need a set of 6 ads of the following sizes created for Bidwave:

Medium rectangle: 300×250
Leaderboard: 728×90
Wide skyscraper: 160×600
Large rectangle: 300x600
Mobile leaderboard: 320×50
Billboard: 970x250

Here are the Formatting Guidelines (WEB ADS): https://help.bidwave.example/hc/en-us/articles/590213774-Ad-Content-and-Format-Guidelines

No animation - photos to link back to the website.

Here is the website: https://www.veltarenews.example/

Please try to copy the look and feel.

Here are some words for the ad - feel free to use creative liberties if you have something better or need less words.

1. VELTA. Results - Not Recommendations.
2. VELTA. Transform Your Business By Transforming Your Core.
3. It's time for better results. It's time to change your management company. VELTA.
4. What company couldn't benefit from a "fresh set of eyes?" Talk to Velta.
5. Talk to VELTA about what they can do for your bottom-line.

Target Market(s)

People who have already visited our website. These people will be private owners, REITs, or Private Equity people looking for a new management company for their underperforming asset.

Industry/Entity Type

Property Management

Font styles to use
Sans Serif

Colors
f37122
6b449b
33b8a4

Requirements
Must have
• logo - at least the "O" unless you can find other ways to pull it back to the website.
Nice to have
• Photos from veltarenews.example to remind the user what website we are when they are redirected - I purchased from lumvara pictures off brick harbor.
Should not have
• Animation

```html
<!DOCTYPE html>
<html lang="en">
<head>
<meta charset="utf-8">
<title>VELTA Display Ad Set</title>
<link rel="stylesheet" href="https://fonts.googleapis.com/css2?family=Raleway:wght@300;400;700&family=Roboto:wght@400&display=swap">
<style>
  :root {
    --board: #ececec;
    --board-light: #f7f7f7;
    --label: #111111;
    --white: #ffffff;
    --brand-purple: #6b449b;
    --brand-deep: #3d1f63;
    --wood-dark: #3a2c22;
    --wood-mid: #5b4533;
    --wood-light: #8a6a4b;
    --shadow: rgba(0, 0, 0, 0.35);
  }
  * { box-sizing: border-box; margin: 0; padding: 0; }
  html, body { width: 1016px; height: 1200px; overflow: hidden; }
  body {
    position: relative;
    background: radial-gradient(ellipse at 50% 40%, var(--board-light), var(--board));
    font-family: "Raleway", "Century Gothic", sans-serif;
    color: var(--white);
  }
  .size-label {
    position: absolute;
    color: var(--label);
    font-family: "Roboto", Arial, sans-serif;
    font-size: 28px;
    font-weight: 400;
    line-height: 37px;
    text-align: center;
    white-space: nowrap;
  }
  .size-label--left { text-align: left; }

  .ad {
    position: absolute;
    overflow: hidden;
    box-shadow: 0 3px 6px var(--shadow);
  }
  .ad-photo {
    position: absolute; inset: 0;
    background:
      radial-gradient(ellipse at 70% 55%, rgba(214,160,105,0.55), transparent 55%),
      radial-gradient(ellipse at 25% 75%, rgba(196,96,40,0.45), transparent 40%),
      linear-gradient(135deg, var(--wood-dark), var(--wood-mid) 55%, var(--wood-light));
  }
  .ad-frame { position: absolute; inset: 0; width: 100%; height: 100%; }
  .ad-frame .panel { fill: var(--white); }

  .brand {
    position: absolute;
    display: flex;
    align-items: center;
    color: var(--brand-deep);
    font-weight: 700;
    letter-spacing: 0.02em;
  }
  .brand-dot {
    display: block;
    border-radius: 50%;
    background: var(--brand-purple);
  }
  .headline {
    position: absolute;
    font-weight: 300;
    text-align: center;
    white-space: nowrap;
  }
  .cta {
    position: absolute;
    display: flex;
    align-items: center;
    justify-content: center;
    border: 2px solid var(--white);
    font-weight: 400;
    letter-spacing: 0.02em;
    white-space: nowrap;
  }
  .url {
    position: absolute;
    font-weight: 400;
    white-space: nowrap;
  }

  /* Medium rectangle 300x250 */
  .ad--medium { left: 40px; top: 59px; width: 278px; height: 232px; }
  .ad--medium .brand { left: 22px; top: 12px; font-size: 27px; gap: 8px; }
  .ad--medium .brand-dot { width: 24px; height: 24px; }
  .ad--medium .headline { left: 0; width: 100%; top: 88px; font-size: 15px; line-height: 20px; font-weight: 400; }
  .ad--medium .cta { left: 69px; top: 147px; width: 143px; height: 39px; font-size: 17px; }
  .ad--medium .url { left: 0; width: 100%; text-align: center; top: 202px; font-size: 16.5px; }

  /* Large rectangle 300x600 */
  .ad--large { left: 397px; top: 59px; width: 278px; height: 556px; }
  .ad--large .brand { left: 26px; top: 30px; font-size: 36px; gap: 11px; }
  .ad--large .brand-dot { width: 36px; height: 36px; }
  .ad--large .headline { left: 0; width: 100%; top: 144px; font-size: 33px; line-height: 38px; }
  .ad--large .cta { left: 22px; top: 365px; width: 236px; height: 66px; font-size: 29px; border-width: 3px; font-weight: 300; }
  .ad--large .url { left: 0; width: 100%; text-align: center; top: 522px; font-size: 16.5px; }

  /* Wide skyscraper 160x600 */
  .ad--skyscraper { left: 796px; top: 59px; width: 148px; height: 556px; }
  .ad--skyscraper .brand { left: 14px; top: 20px; font-size: 23px; gap: 6px; }
  .ad--skyscraper .brand-dot { width: 22px; height: 22px; }
  .ad--skyscraper .headline { left: 0; width: 100%; top: 170px; }
  .ad--skyscraper .headline span { display: block; }
  .line-xl { font-size: 30px; line-height: 34px; }
  .line-l { font-size: 22px; line-height: 25px; }
  .line-s { font-size: 17px; line-height: 21px; }
  .line-m { font-size: 17.5px; line-height: 21px; }
  .ad--skyscraper .cta { left: 7px; top: 398px; width: 134px; height: 39px; font-size: 16px; }
  .ad--skyscraper .url { left: 0; width: 100%; text-align: center; top: 528px; font-size: 10.5px; }

  /* Mobile leaderboard 320x50 */
  .ad--mobile { left: 49px; top: 501px; width: 296px; height: 46px; }
  .ad--mobile .brand { left: 6px; top: 15px; font-size: 11px; gap: 4px; }
  .ad--mobile .brand-dot { width: 12px; height: 12px; }
  .ad--mobile .headline { left: 81px; top: 5px; font-size: 8px; line-height: 11px; text-align: left; font-weight: 400; }
  .ad--mobile .cta { left: 216px; top: 14px; width: 72px; height: 19px; font-size: 8px; border-width: 1px; }
  .ad--mobile .url { left: 81px; top: 29px; font-size: 7.5px; }

  /* Leaderboard 728x90 */
  .ad--leaderboard { left: 54px; top: 737px; width: 674px; height: 83px; }
  .ad--leaderboard .brand { left: 13px; top: 27px; font-size: 27px; gap: 9px; }
  .ad--leaderboard .brand-dot { width: 27px; height: 27px; }
  .ad--leaderboard .headline { left: 200px; top: 8px; font-size: 17px; line-height: 23px; text-align: left; }
  .ad--leaderboard .cta { left: 496px; top: 21px; width: 152px; height: 44px; font-size: 18px; }
  .ad--leaderboard .url { left: 200px; top: 56px; font-size: 14px; letter-spacing: 0.12em; }

  /* Billboard 970x250 */
  .ad--billboard { left: 54px; top: 903px; width: 897px; height: 232px; }
  .ad--billboard .brand { left: 19px; top: 85px; font-size: 50px; gap: 20px; }
  .ad--billboard .brand-dot { width: 56px; height: 56px; }
  .ad--billboard .headline { left: 336px; width: 560px; top: 8px; font-size: 32px; line-height: 39px; }
  .ad--billboard .cta { left: 490px; top: 110px; width: 252px; height: 69px; font-size: 30px; border-width: 3px; font-weight: 300; }
  .ad--billboard .url { left: 336px; width: 560px; text-align: center; top: 187px; font-size: 23px; letter-spacing: 0.1em; }
</style>
</head>
<body>

  <div class="ad ad--medium">
    <div class="ad-photo" role="img" aria-label="Wooden tangram pieces on a dark wood table"></div>
    <svg class="ad-frame" viewBox="0 0 278 232" preserveAspectRatio="none" aria-hidden="true">
      <polygon class="panel" points="0,0 230,0 169,78 0,78"/>
    </svg>
    <div class="brand"><span class="brand-dot"></span>VELTA</div>
    <p class="headline">VELTA Transform Your Business<br>By Transforming The Core</p>
    <div class="cta">LET’S TALK</div>
    <p class="url">www.veltarenews.example</p>
  </div>
  <div class="size-label" style="left:30px;top:336px;width:294px;">Medium Rectangel<br>300x250</div>

  <div class="ad ad--large">
    <div class="ad-photo" role="img" aria-label="Wooden tangram pieces on a dark wood table"></div>
    <svg class="ad-frame" viewBox="0 0 278 556" preserveAspectRatio="none" aria-hidden="true">
      <polygon class="panel" points="0,0 275,0 209,114 0,114"/>
    </svg>
    <div class="brand"><span class="brand-dot"></span>VELTA</div>
    <p class="headline">VELTA<br>Transform Your<br>Business By<br>Transforming<br>The Core</p>
    <div class="cta">LET’S TALK</div>
    <p class="url">www.veltarenews.example</p>
  </div>
  <div class="size-label" style="left:380px;top:624px;width:314px;">Large Rectangle<br>300x600</div>

  <div class="ad ad--skyscraper">
    <div class="ad-photo" role="img" aria-label="Wooden tangram pieces on a dark wood table"></div>
    <svg class="ad-frame" viewBox="0 0 148 556" preserveAspectRatio="none" aria-hidden="true">
      <polygon class="panel" points="0,0 148,0 148,58 103,102 0,102"/>
    </svg>
    <div class="brand"><span class="brand-dot"></span>VELTA</div>
    <p class="headline">
      <span class="line-xl">VELTA</span>
      <span class="line-l">Transform</span>
      <span class="line-s">Your</span>
      <span class="line-l">Business</span>
      <span class="line-s">By</span>
      <span class="line-m">Transforming</span>
      <span class="line-m">The Core</span>
    </p>
    <div class="cta">LET’S TALK</div>
    <p class="url">www.veltarenews.example</p>
  </div>
  <div class="size-label" style="left:740px;top:635px;width:260px;">WIde SKyscraper<br>160x600</div>

  <div class="ad ad--mobile">
    <div class="ad-photo" role="img" aria-label="Wooden tangram pieces on a dark wood table"></div>
    <svg class="ad-frame" viewBox="0 0 296 46" preserveAspectRatio="none" aria-hidden="true">
      <polygon class="panel" points="0,0 66,0 78,23 66,46 0,46"/>
    </svg>
    <div class="brand"><span class="brand-dot"></span>VELTA</div>
    <p class="headline">VELTA Transform Your Business<br>By Transforming The Core</p>
    <div class="cta">LET’S TALK</div>
    <p class="url">www.veltarenews.example</p>
  </div>
  <div class="size-label" style="left:40px;top:559px;width:314px;">Mobile Leaderboard<br>320x50</div>

  <div class="size-label size-label--left" style="left:61px;top:694px;">Leader Board 728x90</div>
  <div class="ad ad--leaderboard">
    <div class="ad-photo" role="img" aria-label="Wooden tangram pieces on a dark wood table"></div>
    <svg class="ad-frame" viewBox="0 0 674 83" preserveAspectRatio="none" aria-hidden="true">
      <polygon class="panel" points="0,0 152,0 178,41.5 152,83 0,83"/>
    </svg>
    <div class="brand"><span class="brand-dot"></span>VELTA</div>
    <p class="headline">VELTA Transform Your Business<br>By Transforming The Core</p>
    <div class="cta">LET’S TALK</div>
    <p class="url">www.veltarenews.example</p>
  </div>

  <div class="size-label size-label--left" style="left:57px;top:854px;">BIllboard 970x250</div>
  <div class="ad ad--billboard">
    <div class="ad-photo" role="img" aria-label="Wooden tangram pieces on a dark wood table"></div>
    <svg class="ad-frame" viewBox="0 0 897 232" preserveAspectRatio="none" aria-hidden="true">
      <polygon class="panel" points="0,0 243,0 357,116 243,232 0,232"/>
    </svg>
    <div class="brand"><span class="brand-dot"></span>VELTA</div>
    <p class="headline">VELTA Transform Your Business<br>By Transforming The Core</p>
    <div class="cta">LET’S TALK</div>
    <p class="url">www.veltarenews.example</p>
  </div>

</body>
</html>
```